Ruvo's Enchilada Special

Ruvo's Restaurant is looking for a flyer design for an Enchilada Special. We wanna thank our loyal customers for preferring us , and invite new ones .
The price is gonna be $3.99
we also would like to invite people to like us on facebook .
facebook.com/ruvosrestaurant
We want the logo to be present and the Enchiladas picture too .
thank you .
Updates
Ruvo's
418 N. 263
Almira Flats, Calvera 40291
555-555-0148
THANK YOU EVERYONE FOR POSTING YOUR DESIGNS .. I WAS VERY HAPPY WITH ALL THE DESIGNS .. I WAS LOOKING FOR SOMETHING SIMPLE AND I ALREADY MADE A PICK.. I SAW SOME GREAT DESIGNS WITH ALOT OF POTENTIAL FOR OTHER PROJECTS .. ILL BE POSTING A MENU COVER BY THIS WEEK .. I HOPE YOU CAN ALL PARTICIPATE . THANK YOU AND FORGIVE ME FOR NOT BEING ABLE TO GIVE TO MUCH FEEDBACK BUT ITS BEEN ONE CRAZY WEEK . THANKS RUVO

```html
<!DOCTYPE html>
<html lang="en">
<head>
<meta charset="utf-8">
<title>Ruvo's Enchilada Special</title>
<link rel="stylesheet" href="https://fonts.googleapis.com/css2?family=Lobster+Two:ital,wght@0,700;1,700&family=Archivo+Narrow:wght@700&family=Oswald:wght@600&display=swap">
<style>
  :root {
    --backdrop: #4a3526;
    --green: #1e7a3c;
    --green-deep: #155f2c;
    --green-light: #2f9c52;
    --green-text: #3aa357;
    --parchment: #dcc48c;
    --parchment-light: #ecdcaa;
    --gold: #f6d238;
    --orange: #f39a1e;
    --red: #e8262b;
    --ink: #2a2522;
    --brown: #5a3b1a;
    --social-blue: #3b5998;
  }
  * { margin: 0; padding: 0; box-sizing: border-box; }
  html, body { width: 858px; height: 1200px; overflow: hidden; }
  body { background: var(--backdrop); position: relative; }

  .flyer {
    position: absolute; left: 21px; top: 20px;
    width: 815px; height: 1160px; overflow: hidden;
    background: radial-gradient(ellipse at 50% 40%, var(--parchment-light), var(--parchment) 70%, #c9ad6e);
  }
  .header-band {
    position: absolute; left: 0; top: 0; width: 100%; height: 46px;
    background: var(--green); border-bottom: 3px solid var(--gold);
  }
  .header-burst { position: absolute; left: 172px; top: -20px; width: 470px; height: 297px; }
  .thanks {
    position: absolute; top: 10px;
    font: italic 700 23px "Lobster Two", cursive; color: var(--green-text);
  }
  .thanks--left { left: 257px; }
  .thanks--right { left: 451px; }
  .brand-mark {
    position: absolute; left: 367px; top: 40px; width: 80px; height: 80px;
    border-radius: 50%; background: var(--orange);
  }
  .brand-name {
    position: absolute; left: 0; width: 100%; top: 134px; text-align: center;
    font: 700 52px "Lobster Two", cursive; color: var(--orange);
  }

  .social-label {
    position: absolute; left: 41px; top: 96px;
    font: italic 700 18px "Lobster Two", cursive; color: var(--brown);
  }
  .social-square {
    position: absolute; left: 62px; top: 131px; width: 57px; height: 57px;
    border-radius: 6px; background: var(--social-blue);
    box-shadow: 0 2px 4px rgba(0,0,0,.35);
  }

  .invite {
    position: absolute; left: 401px; top: 335px; transform: translate(-50%, -50%) rotate(-8deg);
    font: italic 700 38px "Lobster Two", cursive; color: var(--green); white-space: nowrap;
  }
  .headline {
    position: absolute; left: 403px; top: 420px; transform: translate(-50%, -50%) rotate(-11deg);
    font: italic 700 90px "Lobster Two", cursive; color: var(--ink); white-space: nowrap;
  }

  .footer-panel { position: absolute; left: 0; top: 0; width: 815px; height: 1160px; }

  .dish-photo {
    position: absolute; left: 45px; top: 490px; width: 740px; height: 460px;
    border-radius: 50%;
    background: radial-gradient(ellipse at 55% 62%, #f2d24a 0%, #d9502a 28%, #b83a24 40%, rgba(240,236,228,.9) 52%, rgba(120,150,60,.5) 64%, rgba(200,60,40,0) 74%);
  }

  .price-badge { position: absolute; left: 521px; top: 829px; width: 240px; height: 236px; }
  .price {
    position: absolute; left: 641px; top: 947px; transform: translate(-50%, -50%) rotate(-5deg);
    font: 600 72px "Oswald", sans-serif; color: var(--gold); white-space: nowrap;
  }

  .contact { position: absolute; left: 59px; top: 978px; color: var(--gold); font-style: normal; }
  .contact-name { font: italic 700 40px "Lobster Two", cursive; margin-bottom: 2px; }
  .contact-line { font: 700 20px/1.4 "Archivo Narrow", sans-serif; white-space: nowrap; }
</style>
</head>
<body>
  <main class="flyer">
    <svg class="footer-panel" viewBox="0 0 815 1160" aria-hidden="true">
      <defs>
        <radialGradient id="footerGlow" cx="0.55" cy="1" r="0.9">
          <stop offset="0" stop-color="#2f9c52"/>
          <stop offset="1" stop-color="#155f2c"/>
        </radialGradient>
      </defs>
      <path d="M0 905 Q 480 890 815 650 L815 1160 L0 1160 Z" fill="var(--orange)"/>
      <path d="M0 912 Q 480 897 815 660 L815 1160 L0 1160 Z" fill="var(--gold)"/>
      <path d="M0 920 Q 480 905 815 672 L815 1160 L0 1160 Z" fill="url(#footerGlow)"/>
    </svg>

    <div class="dish-photo" role="img" aria-label="Photo of the enchilada plate with beans and rice, surrounded by red, green and yellow chili peppers"></div>

    <div class="header-band"></div>
    <svg class="header-burst" viewBox="-1 -1 2 2" preserveAspectRatio="none" aria-hidden="true">
      <polygon fill="var(--green)" stroke="var(--gold)" stroke-width="2" vector-effect="non-scaling-stroke"
        points="1,-1 1,0 .853,.112 .966,.259 .795,.329 .866,.5 .682,.524 .707,.707 .524,.682 .5,.866 .329,.795 .259,.966 .112,.853 0,1 -.112,.853 -.259,.966 -.329,.795 -.5,.866 -.524,.682 -.707,.707 -.682,.524 -.866,.5 -.795,.329 -.966,.259 -.853,.112 -1,0 -1,-1"/>
    </svg>
    <p class="thanks thanks--left">Thank you</p>
    <p class="thanks thanks--right">for choosing</p>
    <div class="brand-mark"></div>
    <h2 class="brand-name">Ruvo's</h2>

    <p class="social-label">Join us on</p>
    <div class="social-square"></div>

    <p class="invite">Visit us and enjoy</p>
    <h1 class="headline">Enchilada Special</h1>

    <svg class="price-badge" viewBox="-1 -1 2 2" preserveAspectRatio="none" aria-hidden="true">
      <polygon fill="var(--red)"
        points="1,0 .853,.112 .966,.259 .795,.329 .866,.5 .682,.524 .707,.707 .524,.682 .5,.866 .329,.795 .259,.966 .112,.853 0,1 -.112,.853 -.259,.966 -.329,.795 -.5,.866 -.524,.682 -.707,.707 -.682,.524 -.866,.5 -.795,.329 -.966,.259 -.853,.112 -1,0 -.853,-.112 -.966,-.259 -.795,-.329 -.866,-.5 -.682,-.524 -.707,-.707 -.524,-.682 -.5,-.866 -.329,-.795 -.259,-.966 -.112,-.853 0,-1 .112,-.853 .259,-.966 .329,-.795 .5,-.866 .524,-.682 .707,-.707 .682,-.524 .866,-.5 .795,-.329 .966,-.259 .853,-.112"/>
    </svg>
    <p class="price">$3.99</p>

    <address class="contact">
      <p class="contact-name">Ruvo's</p>
      <p class="contact-line">418 N. 263</p>
      <p class="contact-line">Almira Flats, Calvera 40291</p>
      <p class="contact-line">555-555-0148</p>
    </address>
  </main>
</body>
</html>
```